Website for Cannabis Investment Fund *

We need to create a website for our fund which invests in cannabis projects

Industry/Entity Type

Cannabis

Coding

Coded - Design and coding required

Number of Pages Required

1 page

Colors

Designer to choose only greyscale colors for use in the design.

Requirements
Must have
• Please see the attached file

```html
<!DOCTYPE html>
<html lang="en">
<head>
<meta charset="utf-8">
<title>VerdeHarbor Capital</title>
<link rel="stylesheet" href="https://fonts.googleapis.com/css2?family=Montserrat:wght@400;600;700&family=Playfair+Display:wght@700&family=Raleway:wght@400;500;600&display=swap">
<style>
:root{
  --green:#3aaa35;
  --green-dark:#1f5e1a;
  --teal:#3cb5c4;
  --olive:#8aa12b;
  --orange:#f39a1e;
  --red:#e8442a;
  --ink:#222;
  --text:#666;
  --muted:#999;
  --grey-bg:#f0f0f0;
  --line:#e2e2e2;
  --dark:#2e2e2e;
  --darker:#262626;
  --white:#fff;
}
*{box-sizing:border-box;margin:0;padding:0}
html,body{width:1200px;height:4260px;overflow:hidden}
body{position:relative;font-family:'Raleway',sans-serif;color:var(--text);background:var(--white)}
.abs{position:absolute}
h2.section-title{font-family:'Montserrat',sans-serif;font-weight:700;color:var(--ink);text-align:center;font-size:44px;line-height:1.3}

/* hero */
.hero{left:0;top:0;width:1200px;height:620px;background:radial-gradient(ellipse at 60% 40%,#4f9a3a 0%,#2f6f25 45%,#173f14 100%)}
.nav{left:0;top:40px;width:1200px;height:50px}
.nav a{position:absolute;top:14px;color:var(--white);font-family:'Montserrat',sans-serif;font-size:15px;text-decoration:none;letter-spacing:.5px}
.brand{position:absolute;left:0;width:1200px;top:4px;text-align:center;font-family:'Montserrat',sans-serif;font-weight:700;font-size:34px;color:var(--white)}
.nav-phone{position:absolute;left:964px;top:4px;width:160px;height:42px;border:2px solid var(--white);color:var(--white);font-family:'Montserrat',sans-serif;font-size:14px;display:flex;align-items:center;justify-content:center;gap:8px}
.hero-text{left:180px;top:280px;width:840px;text-align:center;font-family:'Playfair Display',serif;font-weight:700;font-size:40px;line-height:1.3;color:var(--white)}
.play{left:566px;top:434px;width:68px;height:68px;border-radius:50%;background:var(--white);display:flex;align-items:center;justify-content:center}

/* value chain */
.chain{left:0;top:620px;width:1200px;height:1080px;background:var(--grey-bg)}
.chain-card{left:80px;top:220px;width:1040px;height:780px;background:var(--white)}
.step{position:absolute;width:190px}
.step .num{font-family:'Montserrat',sans-serif;font-size:44px;font-weight:400;line-height:1}
.step .name{font-size:22px;margin:14px 0 12px}
.step p{font-size:17px;line-height:1.5;color:var(--text)}
.node{position:absolute;width:140px;height:140px;border-radius:50%;background:var(--white);border:14px solid #e9e9e9;display:flex;align-items:center;justify-content:center}
.node::after{content:"";position:absolute;inset:-14px;border-radius:50%;border:4px solid transparent}
.node-ring{position:absolute;width:124px;height:124px;border-radius:50%;border:8px solid}
.axis{left:0;top:372px;width:1040px;height:2px;background:var(--line)}

/* team */
.team-title{left:0;top:1800px;width:1200px}
.team-sub{left:0;top:1850px;width:1200px;text-align:center;font-size:16px;color:var(--muted)}
.tabs{left:0;top:1892px;width:1200px;display:flex;justify-content:center;gap:38px;font-family:'Montserrat',sans-serif;font-size:15px;font-weight:600;color:var(--ink)}
.tabs .on{color:var(--green)}
.photo{background:linear-gradient(180deg,#8c8a86 0%,#5d5b58 60%,#3b3a38 100%)}
.photo-left{left:80px;top:1988px;width:340px;height:300px}
.photo-right{left:780px;top:1988px;width:340px;height:300px;background:linear-gradient(180deg,#c9b38c 0%,#6f7c88 55%,#2f3a48 100%)}
.photo-main{left:420px;top:1948px;width:360px;height:370px;background:linear-gradient(180deg,#d7d4cf 0%,#8a8580 55%,#3c3b3f 100%);box-shadow:0 6px 20px rgba(0,0,0,.25)}
.member{left:470px;top:2300px;width:260px;height:104px;background:var(--green);color:var(--white);text-align:center;padding-top:18px}
.member .nm{font-family:'Montserrat',sans-serif;font-weight:600;font-size:18px}
.member .role{display:inline-block;margin-top:14px;background:var(--white);color:var(--green);font-size:11px;font-family:'Montserrat',sans-serif;font-weight:600;padding:6px 12px;letter-spacing:.5px}
.arrow{top:2348px;width:40px;height:24px}

/* contact band */
.contact{left:0;top:2480px;width:1200px;height:720px;background:linear-gradient(180deg,#e8eaec 0%,#d5d9dc 48%,#7b9a52 60%,#4b7a2c 78%,#2f5a1c 100%)}
.contact-title{left:0;top:2546px;width:1200px}
.contact-sub{left:320px;top:2626px;width:560px;text-align:center;font-size:17px;line-height:1.5;color:var(--text)}
.btn{position:absolute;height:52px;display:flex;align-items:center;justify-content:center;font-family:'Montserrat',sans-serif;font-size:14px;font-weight:600;letter-spacing:.5px}
.btn-fill{background:var(--green);color:var(--white)}
.btn-line{border:2px solid var(--green);color:var(--green);background:rgba(255,255,255,.4)}

/* get in touch */
.touch-box{left:80px;top:3232px;width:484px;height:556px;border:12px solid var(--green);border-left:none;border-top:none;background:var(--white)}
.touch-inner{left:80px;top:3232px;width:472px;height:544px;background:var(--white);box-shadow:0 4px 18px rgba(0,0,0,.08);padding:50px 0 0 0}
.touch-title{left:80px;top:3310px;font-family:'Montserrat',sans-serif;font-weight:700;font-size:40px;color:var(--ink)}
.touch-sub{left:80px;top:3378px;width:220px;font-size:16px;line-height:1.5;color:var(--muted)}
.info{position:absolute;left:80px;display:flex;align-items:center;gap:24px;font-size:15px;color:var(--text)}
.dot{width:48px;height:48px;border-radius:50%;background:var(--green);display:flex;align-items:center;justify-content:center}
.social{position:absolute;top:3656px;width:52px;height:52px;border-radius:50%}
.form{left:660px;top:3240px;width:460px;height:560px;background:var(--white);box-shadow:0 4px 18px rgba(0,0,0,.08)}
.field{position:absolute;left:30px;width:400px;height:60px;border:1px solid var(--line);background:#f7f7f7;font-size:15px;color:var(--text);padding:18px 16px}

/* footer */
.footer{left:0;top:3860px;width:1200px;height:400px;background:var(--dark)}
.f-brand{left:80px;top:3940px;font-family:'Montserrat',sans-serif;font-weight:700;font-size:28px;color:var(--white)}
.f-text{left:80px;top:3998px;width:260px;font-size:14px;line-height:1.6;color:#cfcfcf}
.f-head{position:absolute;top:3944px;font-family:'Montserrat',sans-serif;font-weight:600;font-size:20px;color:var(--white)}
.f-links{left:440px;top:3996px;list-style:none;font-size:14px;line-height:2;color:#cfcfcf}
.f-input{left:676px;top:3996px;width:444px;height:52px;background:#474747;color:#bbb;font-size:14px;padding:17px 20px}
.f-btn{left:676px;top:4068px;width:196px}
.copyright{left:0;top:4170px;width:1200px;height:90px;border-top:1px solid #444;background:var(--darker);text-align:center;padding-top:30px;font-size:14px;color:#888}
</style>
</head>
<body>

<section class="abs hero" role="img" aria-label="Close-up photo of green cannabis leaves"></section>
<nav class="abs nav">
  <a style="left:120px">INVESTMENT FOCUS</a>
  <a style="left:332px">TEAM</a>
  <div class="brand">VerdeHarbor Capital</div>
  <a style="left:824px">CONTACTS</a>
  <div class="nav-phone">
    <svg width="14" height="14" viewBox="0 0 24 24"><path d="M6.6 10.8a15 15 0 0 0 6.6 6.6l2.2-2.2c.3-.3.7-.4 1-.2 1.1.4 2.3.6 3.6.6.6 0 1 .4 1 1V20c0 .6-.4 1-1 1A17 17 0 0 1 3 4c0-.6.4-1 1-1h3.5c.6 0 1 .4 1 1 0 1.3.2 2.5.6 3.6.1.3 0 .7-.2 1z" fill="#fff"/></svg>
    +41 555 010 200
  </div>
</nav>
<div class="abs hero-text">Our goal is to leverage growth of the global cannabis industry by investing in public and private equity of companies in this sector</div>
<div class="abs play"><svg width="22" height="24" viewBox="0 0 22 24"><path d="M3 2l17 10L3 22z" fill="#3aaa35"/></svg></div>

<section class="abs chain">
  <h2 class="section-title abs" style="left:0;top:78px;width:1200px">We invest across all steps of the<br>cannabis product value chain</h2>
  <div class="abs chain-card">
    <div class="abs axis"></div>

    <div class="step" style="left:64px;top:52px">
      <div class="num" style="color:var(--teal)">01</div>
      <div class="name" style="color:var(--teal)">Cultivation</div>
      <p>Cultivation facilities – high tech green-house aimed to reduce operational costs...</p>
    </div>
    <div class="step" style="left:584px;top:52px">
      <div class="num" style="color:var(--orange)">03</div>
      <div class="name" style="color:var(--orange)">Value added retail products</div>
      <p>Value added products in several sectors: health and beauty...</p>
    </div>
    <div class="step" style="left:320px;top:496px">
      <div class="num" style="color:var(--olive)">02</div>
      <div class="name" style="color:var(--olive)">Processing</div>
      <p>High quality THC and CBD concentrates used by the producers of FMCG or medical...</p>
    </div>
    <div class="step" style="left:844px;top:496px">
      <div class="num" style="color:var(--red)">04</div>
      <div class="name" style="color:var(--red)">Distribution</div>
      <p>Promising tools of distribution within the cannabis industry: shops, online and delivery...</p>
    </div>

    <div class="node" style="left:58px;top:302px"><div class="node-ring" style="left:-6px;top:-6px;border-color:var(--teal);clip-path:inset(50% 0 0 0)"></div>
      <svg width="56" height="44" viewBox="0 0 56 44"><rect x="4" y="10" width="30" height="20" fill="none" stroke="#3cb5c4" stroke-width="3"/><path d="M34 16h10l8 8v6H34z" fill="none" stroke="#3cb5c4" stroke-width="3"/><circle cx="14" cy="36" r="5" fill="none" stroke="#3cb5c4" stroke-width="3"/><circle cx="42" cy="36" r="5" fill="none" stroke="#3cb5c4" stroke-width="3"/></svg></div>
    <div class="node" style="left:322px;top:302px"><div class="node-ring" style="left:-6px;top:-6px;border-color:var(--olive);clip-path:inset(0 0 50% 0)"></div>
      <svg width="54" height="54" viewBox="0 0 54 54"><circle cx="27" cy="27" r="22" fill="none" stroke="#8aa12b" stroke-width="3"/><circle cx="27" cy="27" r="12" fill="none" stroke="#8aa12b" stroke-width="3"/></svg></div>
    <div class="node" style="left:582px;top:302px"><div class="node-ring" style="left:-6px;top:-6px;border-color:var(--orange);clip-path:inset(50% 0 0 0)"></div>
      <svg width="52" height="50" viewBox="0 0 52 50"><path d="M4 18h44l-4-12H8z" fill="none" stroke="#f39a1e" stroke-width="3"/><rect x="8" y="18" width="36" height="28" fill="none" stroke="#f39a1e" stroke-width="3"/><rect x="20" y="28" width="12" height="18" fill="none" stroke="#f39a1e" stroke-width="3"/></svg></div>
    <div class="node" style="left:842px;top:302px"><div class="node-ring" style="left:-6px;top:-6px;border-color:var(--red);clip-path:inset(0 0 50% 0)"></div>
      <svg width="52" height="52" viewBox="0 0 52 52"><rect x="6" y="16" width="40" height="30" fill="none" stroke="#e8442a" stroke-width="3"/><path d="M6 16l20-10 20 10" fill="none" stroke="#e8442a" stroke-width="3"/><path d="M16 30h20" stroke="#e8442a" stroke-width="3"/></svg></div>
  </div>
</section>

<h2 class="section-title abs team-title">Our Team</h2>
<div class="abs team-sub">Our team consist of professionals in healthcare and financial industry</div>
<div class="abs tabs"><span class="on">ALL</span><span>INVESTMENT TEAM</span><span>ADVISORY BOARD</span></div>
<div class="abs photo photo-left" role="img" aria-label="Portrait photo of a team member"></div>
<div class="abs photo-right" role="img" aria-label="Portrait photo of a team member outdoors"></div>
<div class="abs photo-main" role="img" aria-label="Portrait photo of a team member in a suit"></div>
<div class="abs member"><div class="nm">Lukas Brenner, MD</div><span class="role">CHIEF SCIENTIFIC OFFICER</span></div>
<svg class="abs arrow" style="left:372px" viewBox="0 0 40 24"><path d="M38 12H4M12 4l-8 8 8 8" fill="none" stroke="#333" stroke-width="2"/></svg>
<svg class="abs arrow" style="left:788px" viewBox="0 0 40 24"><path d="M2 12h34M28 4l8 8-8 8" fill="none" stroke="#333" stroke-width="2"/></svg>

<section class="abs contact" role="img" aria-label="Photo of a cannabis field under a pale sky"></section>
<h2 class="section-title abs contact-title">Contact Us</h2>
<div class="abs contact-sub">If you are an investor interested in learning more about our fund, please send us a message</div>
<div class="btn btn-fill" style="left:416px;top:2710px;width:180px">SEND MESSAGE</div>
<div class="btn btn-line" style="left:606px;top:2710px;width:180px">INVESTORS</div>

<div class="abs touch-box"></div>
<div class="abs touch-title">Get In Touch</div>
<div class="abs touch-sub">Ready to learn more? Call or email us to Schedule</div>
<div class="info" style="top:3488px"><span class="dot"><svg width="20" height="20" viewBox="0 0 24 24"><path d="M6.6 10.8a15 15 0 0 0 6.6 6.6l2.2-2.2c.3-.3.7-.4 1-.2 1.1.4 2.3.6 3.6.6.6 0 1 .4 1 1V20c0 .6-.4 1-1 1A17 17 0 0 1 3 4c0-.6.4-1 1-1h3.5c.6 0 1 .4 1 1 0 1.3.2 2.5.6 3.6.1.3 0 .7-.2 1z" fill="#fff"/></svg></span>+41 555 010 200</div>
<div class="info" style="top:3546px"><span class="dot"><svg width="20" height="16" viewBox="0 0 20 16"><rect x="1" y="1" width="18" height="14" fill="none" stroke="#fff" stroke-width="2"/><path d="M1 2l9 7 9-7" fill="none" stroke="#fff" stroke-width="2"/></svg></span>info@verdeharbor.example</div>
<div class="info" style="top:3604px"><span class="dot"><svg width="16" height="22" viewBox="0 0 16 22"><path d="M8 1a7 7 0 0 0-7 7c0 5 7 13 7 13s7-8 7-13a7 7 0 0 0-7-7z" fill="#fff"/><circle cx="8" cy="8" r="2.5" fill="#3aaa35"/></svg></span>Musterweg 12, 6300 Zug, Switzerland</div>
<div class="social" style="left:80px;background:#3b5998"></div>
<div class="social" style="left:144px;background:#2fa8e1"></div>
<div class="social" style="left:208px;background:#1a84bc"></div>

<div class="abs form">
  <div class="field" style="top:30px">Name :</div>
  <div class="field" style="top:110px">Email :</div>
  <div class="field" style="top:190px">Phone :</div>
  <div class="field" style="top:270px;height:160px">Message :</div>
  <div class="btn btn-fill" style="left:30px;top:456px;width:400px;height:60px">SEND MESSAGE</div>
</div>

<footer class="abs footer"></footer>
<div class="abs f-brand">VerdeHarbor Capital</div>
<div class="abs f-text">Lorem ipsum dolor sit amet, consectetur adipiscing elit, sed do eiusmod tempor incididunt.</div>
<div class="f-head" style="left:440px">Quick Links</div>
<ul class="abs f-links"><li>› INVESTMENT FOCUS</li><li>› TEAM</li><li>› CONTACTS</li></ul>
<div class="f-head" style="left:676px">Subscribe Newsletter</div>
<div class="abs f-input">Enter Email Address...</div>
<div class="btn btn-fill f-btn">SUBSCRIBE NOW</div>
<div class="abs copyright">Copyright © VerdeHarbor Capital 2024. All Rights Reserved</div>

</body>
</html>
```